Business card for hedge fund
Vornelle Capital Management
Project: Business card for hedge fund
Business card for hedge fund - Financial Services
Creative Brief
Professional
Wanrudee Halvorsen
Chief Operating Officer
wanru.halvorsen@vornellecap.example
2 additional names: Martin Gaskell, Portfolio Manager p: +1-555-382-4719 e-mail: martin.gaskell@vornellecap.example Jia Luo, Portfolio Manager p: +852-5123-9046 e: jia.luo@vornellecap.example No address to be included

```html
<!DOCTYPE html>
<html lang="en">
<head>
<meta charset="utf-8">
<title>Vornelle Capital Management – Business Card</title>
<link rel="stylesheet" href="https://fonts.googleapis.com/css2?family=Cinzel:wght@400&family=Open+Sans:wght@400;600;700&display=swap">
<style>
  :root {
    --stage: #e4e4e4;
    --card-dark: #3a3a3a;
    --card-dark-edge: #2b2b2b;
    --white: #ffffff;
    --paper-shade: #ececec;
    --band-grey: #4a4a4a;
    --orange: #f2a51c;
    --orange-deep: #e08a0c;
    --ink: #3b3b3b;
    --ink-soft: #6a6a6a;
  }
  * { box-sizing: border-box; margin: 0; padding: 0; }
  html, body { width: 1200px; height: 864px; overflow: hidden; }
  body {
    background: var(--stage);
    position: relative;
    font-family: "Open Sans", Arial, sans-serif;
  }
  .card {
    position: absolute;
    left: 250px;
    width: 700px;
    height: 400px;
    border-radius: 26px;
    overflow: hidden;
    box-shadow: 0 6px 18px rgba(0,0,0,.18);
  }

  /* Back of card */
  .card-back {
    top: 20px;
    background: radial-gradient(ellipse at 50% 40%, var(--card-dark) 0%, var(--card-dark-edge) 100%);
    display: flex;
    align-items: center;
    justify-content: center;
  }
  .card-back .brand-name {
    font-family: "Cinzel", Georgia, serif;
    font-weight: 400;
    color: var(--white);
    font-size: 40px;
    letter-spacing: 4px;
    text-transform: uppercase;
    text-align: center;
    line-height: 1.3;
  }

  /* Front of card */
  .card-front {
    top: 444px;
    background: radial-gradient(ellipse at 30% 30%, var(--white) 40%, var(--paper-shade) 100%);
  }
  .card-front .band { position: absolute; inset: 0; width: 100%; height: 100%; }

  .brand {
    position: absolute;
    left: 64px;
    top: 96px;
    display: flex;
    align-items: center;
    gap: 14px;
  }
  .brand-dot {
    width: 34px; height: 34px; border-radius: 50%;
    background: var(--ink);
    flex: none;
  }
  .brand .brand-name {
    font-family: "Cinzel", Georgia, serif;
    font-weight: 400;
    color: var(--ink);
    font-size: 23px;
    line-height: 1.2;
    letter-spacing: 1px;
    text-transform: uppercase;
    width: 250px;
  }

  .person {
    position: absolute;
    left: 112px;
    top: 218px;
  }
  .person-name {
    font-weight: 700;
    font-size: 15px;
    color: var(--ink);
  }
  .person-title {
    font-weight: 400;
    font-size: 12px;
    color: var(--ink-soft);
    margin-top: 2px;
  }

  .contact {
    position: absolute;
    left: 420px;
    top: 96px;
    width: 250px;
    list-style: none;
  }
  .contact li {
    display: flex;
    align-items: center;
    gap: 8px;
    font-size: 11.5px;
    color: var(--ink);
    height: 19px;
    white-space: nowrap;
  }
  .contact-icon {
    width: 13px; height: 13px;
    border-radius: 50%;
    background: var(--ink);
    flex: none;
    display: flex; align-items: center; justify-content: center;
  }
  .contact-icon svg { width: 8px; height: 8px; fill: var(--white); }
</style>
</head>
<body>

  <section class="card card-back">
    <p class="brand-name">Vornelle<br>Capital Management</p>
  </section>

  <section class="card card-front">
    <svg class="band" viewBox="0 0 700 400" preserveAspectRatio="none" aria-hidden="true">
      <defs>
        <linearGradient id="orangeSweep" x1="0" y1="1" x2="1" y2="0">
          <stop offset="0" stop-color="var(--orange-deep)"/>
          <stop offset="1" stop-color="var(--orange)"/>
        </linearGradient>
      </defs>
      <path d="M0 300 C 200 340 420 320 700 210 L700 400 L0 400 Z" fill="var(--band-grey)"/>
      <path d="M230 400 C 430 380 580 320 700 238 L700 400 Z" fill="url(#orangeSweep)"/>
      <path d="M0 296 C 200 336 420 316 700 206 L700 214 C 420 326 200 346 0 306 Z" fill="var(--white)"/>
    </svg>

    <div class="brand">
      <span class="brand-dot"></span>
      <p class="brand-name">Vornelle Capital Management</p>
    </div>

    <div class="person">
      <p class="person-name">Wanrudee Halvorsen</p>
      <p class="person-title">Chief Operating Officer</p>
    </div>

    <ul class="contact">
      <li><span class="contact-icon"><svg viewBox="0 0 10 10"><path d="M2 1l2 2-1 1c.6 1.2 1.8 2.4 3 3l1-1 2 2-1.5 1.5C4.5 9 1 5.5.5 2.5z"/></svg></span>+1-555-786-5830</li>
      <li><span class="contact-icon"><svg viewBox="0 0 10 10"><path d="M2 1l2 2-1 1c.6 1.2 1.8 2.4 3 3l1-1 2 2-1.5 1.5C4.5 9 1 5.5.5 2.5z"/></svg></span>+1-555-567-8910</li>
      <li><span class="contact-icon"><svg viewBox="0 0 10 10"><path d="M2 1l2 2-1 1c.6 1.2 1.8 2.4 3 3l1-1 2 2-1.5 1.5C4.5 9 1 5.5.5 2.5z"/></svg></span>+1-555-654-3210</li>
      <li><span class="contact-icon"><svg viewBox="0 0 10 10"><path d="M1 2.5h8v5H1z M1 2.5l4 3 4-3"/></svg></span>wanru.halvorsen@vornellecap.example</li>
      <li><span class="contact-icon"><svg viewBox="0 0 10 10"><circle cx="5" cy="5" r="3.5"/></svg></span>www.vornellecap.example</li>
    </ul>
  </section>

</body>
</html>
```